A4 Wholesale Catalogue for a Hardware Supply Company

We are a tarpaulin manufacture and supply company. We need a A4 multi page catalogue to be used as a selling tool for our wholesale customers. We want the catalogue to be easily understandable but also eye catching.

This catalogue will be used by local hardware stores to sell our products to their account customers. The idea of this catalogue is to enable the hardware store to have a snapshot of our products that will be relevant to their customers whom are largely builders. This will be not be given out to their customer and will be used only in store as a selling tool.

Industry/Entity Type

Building

Font styles to use
Serif

Requirements
Must have
• Detail as per supplied brief.
• Photos
• Branding
Should not have
• To many tables

```html
<!DOCTYPE html>
<html lang="en">
<head>
<meta charset="utf-8">
<title>Roof Tarps – Catalogue Page</title>
<link href="https://fonts.googleapis.com/css2?family=Source+Serif+4:opsz,wght@8..60,400&display=swap" rel="stylesheet">
<style>
  :root {
    --page-bg: #e9e6e1;
    --brand-blue: #4169ad;
    --brand-green: #72bb27;
    --white: #ffffff;
    --footer-text: #2a2a2a;
  }
  html, body {
    margin: 0;
    padding: 0;
    width: 1200px;
    height: 1200px;
    overflow: hidden;
    background: var(--page-bg);
    font-family: "Source Serif 4", serif;
  }
  .catalogue-page {
    position: absolute;
    left: 204px;
    top: 40px;
    width: 792px;
    height: 1120px;
    background: var(--white);
    box-shadow: 0 6px 18px rgba(0,0,0,0.25);
    overflow: hidden;
  }
  .photo {
    position: absolute;
  }
  .photo--aisle {
    left: 0; top: 0; width: 394px; height: 739px;
    background: linear-gradient(90deg,
      #e4e6e9 0%, #6f747a 10%, #c9cdd2 18%, #8a9098 28%,
      #dfe2e5 38%, #7d8690 48%, #b8bec6 55%,
      #a3acb6 62%, #c4cbd3 75%, #c9d0d6 100%);
  }
  .photo--racking {
    left: 396px; top: 0; width: 396px; height: 369px;
    background: linear-gradient(180deg,
      #8f918c 0%, #c9ccc8 12%, #7a7f83 22%,
      #2c3340 32%, #d9dde2 40%, #2455b8 52%,
      #1e2a3c 62%, #2b5fc4 72%, #1d4ea8 82%,
      #c6d0da 92%, #d4dbe2 100%);
  }
  .photo--workshop {
    left: 396px; top: 371px; width: 396px; height: 368px;
    background: linear-gradient(180deg,
      #8b8e8e 0%, #c7c9c6 10%, #3f7e78 25%,
      #b84a3a 32%, #2d4f9c 40%, #bfc6cc 52%,
      #cdd3d8 68%, #9a9fa4 82%, #b3b8bd 100%);
  }
  .title-band {
    position: absolute;
    left: 0; top: 626px;
    width: 594px; height: 75px;
    background: var(--brand-blue);
    display: flex;
    align-items: center;
  }
  .title-band h1 {
    margin: 0 0 0 35px;
    font-weight: 400;
    font-size: 34px;
    color: var(--white);
    letter-spacing: 0.5px;
  }
  .accent-block {
    position: absolute;
    left: 594px; top: 626px;
    width: 198px; height: 75px;
    background: var(--brand-green);
  }
  .body-panel {
    position: absolute;
    left: 0; top: 739px;
    width: 792px; height: 342px;
    background: var(--brand-blue);
    box-sizing: border-box;
    padding: 40px 38px 0 37px;
    color: var(--white);
    font-size: 13.5px;
    line-height: 15.8px;
  }
  .body-panel p {
    margin: 0 0 16px;
  }
  .page-footer {
    position: absolute;
    left: 0; top: 1081px;
    width: 792px; height: 39px;
    display: flex;
    align-items: center;
    justify-content: center;
    color: var(--footer-text);
    font-size: 16.5px;
  }
</style>
</head>
<body>
  <main class="catalogue-page">
    <div class="photo photo--aisle" role="img" aria-label="Warehouse aisle lined with stacked packaged tarps"></div>
    <div class="photo photo--racking" role="img" aria-label="Warehouse racking stocked with blue, black and white tarps"></div>
    <div class="photo photo--workshop" role="img" aria-label="Workshop floor with a large tarp laid out for fabrication"></div>

    <div class="title-band"><h1>ROOF TARPS</h1></div>
    <div class="accent-block"></div>

    <section class="body-panel">
      <p>We have a huge range of roof tarps available to suit any building project big or small for the short or long term. Ultimately, all of our tarps are suitable for covering roofs. Which one is most suitable depends on the job and preference of the builder.</p>
      <p>PVC tarps are great as they are extremely durable, repairable and heavy enough to stay down on the roof and are less prone to flapping.</p>
      <p>The main disadvantage is obviously the upfront cost and the limited size due to the weight of the fabric. Generally we feel that anything over 55kgs becomes unmanageable which is why we don't have standard sizes bigger than what is displayed in each grade.</p>
      <p>Poly Tarps can be more suitable than PVC tarps as they are more cost effective, available in larger sizes and therefore require less tying down and overlapping. They can also be used for covering timber/ sand etc when they have become well worn.</p>
      <p>We have selected our most popular sizes as a guide as every house is different we do have sizes ranging from 1.8m x 2.4m up to 25.0m x 60.0n, so if you cannot find your required size please ask!</p>
    </section>

    <footer class="page-footer">7A/21 Carrow Street &nbsp;|&nbsp; Westbrook NSW 2190 &nbsp;|&nbsp; info@baylinetarps.com.au</footer>
  </main>
</body>
</html>
```